creation of business cards for Velanto Sàrl

Velanto S% 26 # 224; rl is a soci% 26 # 233; t% 26 # 233; consultancy that accompanies companies in the development of their business on the market% 26 # 233; Switzerland by providing strategic contacts or market information; and by providing administrative or logistical support. Our consulting skills focus on sectors% 26 # 224; high value added% 26 # 233; e, such as trade in food goods% 26 # 39amp; drinks, fashion% 26amp; lifestyle, products and services for% 26 # 233; s in high-tech industries (pharmaceutical, chemical, m% 26 # 233; pricy 26% 23 #; cision) or sustainable solutions (% 26 # 233; energies renewable, mat% 26 # 233; recyclable materials). As part of the launch of our activity% 26 # 233;, we need% 26 # 39;% 26 # 233; to establish business cards to d% 26 # 233; work our new customers (Swiss or international).

Target Market(s)

Companies wishing to develop their activity% 26 # 233; s in Switzerland or% 26 # 224; l% 26 # 39;% 26 # 233; abroad (mainly in Europe).

Contact Information for Business Card

Prénom NOM
Velanto Sàrl
Bureau de Marvoisin
Rue des Tilleuls 47, 2000 Neuchâtel
Tél. : 032 718 46 39
info@velanto-example.ch
www.velanto-example.ch

Font styles to use
Serif
Sans Serif

Colors

Designer to choose colors to be used in the design.

Requirements
Must have
• The logo The name of the company% 26 # 233; t% 26 # 233; (Velanto S% 26 # 224; rl) One field for the mailing address One field for the number% 26 # 233; ro de t% 26 # 233; l% 26 # 233; phone One field for the % 26 # 39; email address and website

```html
<!DOCTYPE html>
<html lang="fr">
<head>
<meta charset="utf-8">
<title>Velanto Sàrl – cartes de visite</title>
<link rel="stylesheet" href="https://fonts.googleapis.com/css2?family=Montserrat:wght@300;400;700&family=Open+Sans:wght@400&display=swap">
<style>
  :root {
    --teal: #003f5a;
    --teal-deep: #00364d;
    --paper: #ffffff;
    --ink-grey: #6a6a6a;
    --rule: #7a7a7a;
    --backdrop: #d6d5d1;
  }
  * { box-sizing: border-box; margin: 0; padding: 0; }
  html, body { width: 1200px; height: 801px; overflow: hidden; }
  body {
    background: var(--backdrop);
    font-family: "Open Sans", Arial, sans-serif;
    position: relative;
  }
  .card {
    position: absolute;
    top: 232px;
    width: 520px;
    height: 336px;
    box-shadow: 0 6px 18px rgba(0,0,0,.18);
  }
  .card--front { left: 60px; background: var(--paper); }
  .card--back {
    left: 620px;
    background: linear-gradient(160deg, var(--teal) 0%, var(--teal-deep) 100%);
    display: flex; align-items: center; justify-content: center;
  }

  .brand { display: flex; align-items: center; gap: 14px; }
  .brand__mark { width: 34px; height: 34px; background: var(--teal); border-radius: 7px; }
  .brand__name {
    font-family: "Montserrat", Arial, sans-serif;
    font-weight: 300;
    font-size: 27px;
    letter-spacing: 3px;
    color: var(--teal);
  }
  .card--front .brand { position: absolute; left: 30px; top: 150px; }
  .card--back .brand { gap: 26px; }
  .card--back .brand__mark { width: 62px; height: 62px; background: var(--paper); border-radius: 13px; }
  .card--back .brand__name { font-size: 46px; letter-spacing: 5px; color: var(--paper); }

  .divider {
    position: absolute; left: 250px; top: 86px;
    width: 1px; height: 164px; background: var(--rule);
  }
  .contact { position: absolute; left: 266px; top: 88px; width: 240px; }
  .contact__name {
    font-family: "Montserrat", Arial, sans-serif;
    font-weight: 700; font-size: 19px; color: var(--teal); line-height: 1.15;
  }
  .contact__company { font-size: 14px; color: var(--ink-grey); margin-bottom: 8px; }
  .contact__line { font-size: 11px; color: var(--ink-grey); line-height: 1.55; }
  .contact__item { display: flex; align-items: center; gap: 6px; }
  .contact__icon { width: 11px; height: 11px; flex: none; }
</style>
</head>
<body>

<section class="card card--front" aria-label="Recto">
  <div class="brand">
    <span class="brand__mark"></span>
    <span class="brand__name">VELANTO</span>
  </div>
  <div class="divider"></div>
  <div class="contact">
    <p class="contact__name">Prénom NOM</p>
    <p class="contact__company">Velanto Sàrl</p>
    <p class="contact__line">Bureau de Marvoisin</p>
    <p class="contact__line">Rue des Tilleuls 47, 2000 Neuchâtel</p>
    <p class="contact__line contact__item">
      <svg class="contact__icon" viewBox="0 0 12 12"><circle cx="6" cy="6" r="6" fill="#003f5a"/><path d="M3.6 3.2c.4-.3.8-.3 1 .1l.5.9c.1.3 0 .5-.2.7l-.3.2c.3.7.9 1.3 1.6 1.6l.2-.3c.2-.2.4-.3.7-.2l.9.5c.4.2.4.6.1 1-.6.6-1.4.6-2.2.2A6 6 0 0 1 3.4 5.4c-.4-.8-.4-1.6.2-2.2z" fill="#fff"/></svg>
      032 718 46 39
    </p>
    <p class="contact__line contact__item">
      <svg class="contact__icon" viewBox="0 0 12 12"><circle cx="6" cy="6" r="6" fill="#003f5a"/><rect x="3" y="4" width="6" height="4.2" fill="none" stroke="#fff" stroke-width=".8"/><path d="M3 4l3 2.3L9 4" fill="none" stroke="#fff" stroke-width=".8"/></svg>
      info@velanto-example.ch
    </p>
    <p class="contact__line contact__item">
      <svg class="contact__icon" viewBox="0 0 12 12"><circle cx="6" cy="6" r="6" fill="#003f5a"/><circle cx="6" cy="6" r="3.2" fill="none" stroke="#fff" stroke-width=".7"/><ellipse cx="6" cy="6" rx="1.4" ry="3.2" fill="none" stroke="#fff" stroke-width=".7"/><path d="M2.8 6h6.4" stroke="#fff" stroke-width=".7"/></svg>
      www.velanto-example.ch
    </p>
  </div>
</section>

<section class="card card--back" aria-label="Verso">
  <div class="brand">
    <span class="brand__mark"></span>
    <span class="brand__name">VELANTO</span>
  </div>
</section>

</body>
</html>
```